Business Card Design Project

I would like a business card created for a new company. This is a holding company that acts as my investment company. It holds real estate and service based companies. The name of the company is Lucernaria which is Italian for Lanternry. Defined as development or growth.
We currently have no logo. I really like some of the "different" cards out there. Potentially metallic or grey/black. That looks premium/hi-end and unique. I am not sure if your design would be specific to the card stock I end with our just logo/design/font.
Real Estate

```html
<!DOCTYPE html>
<html lang="en">
<head>
<meta charset="utf-8">
<title>Lucernaria — Business Card</title>
<link rel="stylesheet" href="https://fonts.googleapis.com/css2?family=Roboto:wght@400;500;700&display=swap">
<style>
  :root {
    --backdrop: #3a3b3d;
    --card: #121213;
    --card-edge: #1c1c1e;
    --accent: #3cc4e6;
    --text: #d9d9d9;
    --muted: #9a9a9a;
  }
  * { box-sizing: border-box; margin: 0; padding: 0; }
  html, body {
    width: 1067px;
    height: 1200px;
    overflow: hidden;
    background: var(--backdrop);
    font-family: "Roboto", Arial, sans-serif;
  }
  .canvas {
    width: 1067px;
    height: 1200px;
    display: flex;
    flex-direction: column;
    align-items: center;
    justify-content: center;
    gap: 80px;
  }
  .card {
    width: 840px;
    height: 480px;
    background: var(--card);
    border: 1px solid var(--card-edge);
    border-radius: 4px;
    box-shadow: 0 18px 40px rgba(0, 0, 0, 0.45);
    display: flex;
    flex-direction: column;
    align-items: center;
    justify-content: center;
    text-align: center;
  }
  .card--front {
    justify-content: flex-start;
    padding-top: 128px;
  }
  .wordmark {
    color: var(--accent);
    font-weight: 500;
    font-size: 70px;
    letter-spacing: 12px;
    line-height: 1;
  }
  .card--front .wordmark { margin-bottom: 50px; }
  .holder-name {
    color: var(--accent);
    font-weight: 700;
    font-size: 21px;
    letter-spacing: 1px;
  }
  .holder-role {
    color: var(--muted);
    font-size: 13px;
    margin-top: 2px;
    margin-bottom: 18px;
  }
  .address {
    color: var(--text);
    font-size: 15px;
    letter-spacing: 0.5px;
    margin-bottom: 14px;
  }
  .contact-line {
    color: var(--text);
    font-size: 13px;
    letter-spacing: 0.4px;
    line-height: 1.5;
  }
  .contact-line .label { color: var(--accent); margin-left: 14px; }
  .contact-line .label:first-child { margin-left: 0; }
  .website {
    color: var(--accent);
    font-size: 19px;
    letter-spacing: 0.8px;
    margin-top: 6px;
  }
</style>
</head>
<body>
<main class="canvas">
  <section class="card card--front">
    <div class="wordmark">LUCERNARIA</div>
    <div class="holder-name">MARCUS BELLAMY</div>
    <div class="holder-role">Owner</div>
    <div class="address">2480 Alder Row #4, Fairview, CA 00000</div>
    <div class="contact-line">
      <span class="label">c:</span> +1.555.210.4477
      <span class="label">o:</span> +1.555.380.6620 x2047
    </div>
    <div class="contact-line">
      <span class="label">p:</span> +1 (555) 742-9081
      <span class="label">e:</span> marcusbellamy@lucernaria.com
    </div>
    <div class="website">www.lucernariallc.com</div>
  </section>

  <section class="card card--back">
    <div class="wordmark">LUCERNARIA</div>
  </section>
</main>
</body>
</html>
```